Road Wise Community Awareness Poster

We are looking for a tabloid size (11"x17") Poster to be placed all over various towns and communities promoting our business. We need something that grabs the attention of our target demographic (parents of teen drivers) and gets them to want to learn more about our programs and ultimately sign up for one of our events.

see our website for more information at www.roadwisekids.example

Target Market(s)

We want parents of teens ages 15 - 19 to be aware how dangerous driving is for new drivers and compel them to sign their teen up for our program.

Industry/Entity Type

Community

Requirements
Must have
• Must have our logo and identity, url and be 11"x17"

```html
<!DOCTYPE html>
<html lang="en">
<head>
<meta charset="utf-8">
<title>Road Wise Community Awareness Poster</title>
<link rel="stylesheet" href="https://fonts.googleapis.com/css2?family=Anton&family=Open+Sans:ital,wght@0,400;0,600;0,700;1,400&display=swap">
<style>
  :root {
    --green: #3aa744;
    --band-green: #3fac4b;
    --black: #000000;
    --white: #ffffff;
    --ink: #111111;
    --sky: #8fb8d8;
    --foliage: #4f7a2e;
    --dash: #1c1c1c;
  }
  * { margin: 0; padding: 0; box-sizing: border-box; }
  html, body { width: 776px; height: 1200px; overflow: hidden; background: var(--white); }
  .poster { position: relative; width: 776px; height: 1200px; overflow: hidden; background: var(--white); font-family: "Open Sans", Arial, sans-serif; }

  .masthead { position: absolute; top: 0; left: 0; width: 776px; height: 290px; background: var(--black); text-align: center; }
  .headline { padding-top: 24px; font-family: "Anton", Impact, sans-serif; font-weight: 400; color: var(--green); font-size: 78px; line-height: 84px; letter-spacing: 2px; word-spacing: 12px; white-space: nowrap; }
  .subhead { margin-top: 12px; font-family: "Anton", Impact, sans-serif; font-weight: 400; color: var(--white); font-size: 38px; line-height: 46px; letter-spacing: 1px; word-spacing: 6px; white-space: nowrap; }

  .road-photo { position: absolute; top: 290px; left: 0; width: 776px; height: 406px;
    background: linear-gradient(180deg, #1a1a1a 0%, var(--sky) 10%, #cfe0ea 28%, var(--foliage) 45%, #6b7a5a 62%, var(--dash) 74%, #0d0d0d 100%); }
  .photo-caption { position: absolute; top: 466px; left: 0; width: 776px; text-align: center; padding-left: 80px; font-style: italic; color: var(--white); font-size: 24px; white-space: nowrap; }

  .band { position: absolute; top: 696px; left: 0; width: 776px; height: 122px; background: var(--band-green); text-align: center; padding-top: 10px; }
  .band p { font-weight: 700; color: var(--ink); font-size: 40px; line-height: 48px; white-space: nowrap; }
  .band .highlight { color: var(--white); }

  .intro { position: absolute; top: 840px; left: 64px; width: 256px; font-size: 13.5px; line-height: 20px; color: var(--ink); }
  .intro p + p { margin-top: 20px; }

  .features { position: absolute; top: 838px; left: 366px; list-style: none; font-weight: 600; font-size: 21px; line-height: 30.5px; color: var(--ink); white-space: nowrap; }
  .features li::before { content: "• "; }

  .brand { position: absolute; top: 1146px; left: 34px; display: flex; align-items: center; gap: 10px; }
  .brand-mark { width: 22px; height: 22px; border-radius: 50%; background: var(--green); }
  .brand-name { font-weight: 600; font-size: 22px; color: var(--ink); white-space: nowrap; }

  .url { position: absolute; top: 1126px; right: 34px; font-size: 38px; line-height: 56px; color: var(--black); white-space: nowrap; }
</style>
</head>
<body>
<main class="poster">
  <header class="masthead">
    <h1 class="headline">PASSING YOUR TEST<br>WAS THE EASY PART!</h1>
    <p class="subhead">Staying alive is gonna be harder!</p>
  </header>

  <div class="road-photo" role="img" aria-label="Driver's view from inside a car, hands on the steering wheel, looking down an open tree-lined country road"></div>
  <p class="photo-caption">It’s an investment that will last a lifetime!</p>

  <section class="band">
    <p>Just one half-day session can<br>save you or your <span class="highlight">child's life</span></p>
  </section>

  <div class="intro">
    <p>Motor vehicle accidents are the #1 killer of teens nationwide – more than drugs, homicides and suicides combined.</p>
    <p>That doesn't have to be the case — but it is going to take more than the basics to change that.</p>
  </div>

  <ul class="features">
    <li>Skid control</li>
    <li>Advanced speed control</li>
    <li>Crash avoidance</li>
    <li>Winter and bad weather control</li>
    <li>Awareness training</li>
    <li>Advanced Safety</li>
    <li>Speed control</li>
    <li>And best of all lower insurance!!!</li>
  </ul>

  <div class="brand">
    <span class="brand-mark"></span>
    <span class="brand-name">Road Wise</span>
  </div>

  <p class="url">www.roadwisekids.example</p>
</main>
</body>
</html>
```